Brisk Lending - Morgage Broker Website

Hi. I want someone to redesign my website for Brisk Lending, We are a mortgage brokering company in Australia.

I currently have a website www.brisklending.com.au but i do not like the design, I want clean but looking like a nice techie site but with that personal touch still.

I use wordpress and have Elementor Pro installed

Pages like on current site

Target Market(s)

Age Group 30-50, either home owners or looking to buy.

Coding

Coded - Design and coding required

Number of Pages Required

5+ page

Font styles to use
Other font styles liked:
• Ubuntu

Colors
e34298
a54499
e667a6
d3a5cc
b868aa
eea4c8

Requirements
Must have
• My Logo, and branding.. logo attached..
I want something clean and nice and vibrant!
Wordpress!
Mobile Friendly
Contact Forms
Appointment booking button
Call now button
Nice to have
• Mortgage Calculator section, and plenty of CTA's!.

Please do you research on other mortgage broker sites like varopa.com.au

```html
<!DOCTYPE html>
<html lang="en">
<head>
<meta charset="utf-8">
<title>Brisk Lending – Services</title>
<link href="https://fonts.googleapis.com/css2?family=Lato:wght@700&family=Ubuntu:wght@300;400;500;700&display=swap" rel="stylesheet">
<style>
  :root {
    --page-bg: #ffffff;
    --section-bg: #fafafa;
    --card-bg: #f7f7f7;
    --heading: #4a4a4f;
    --body-text: #4d4d55;
    --title-purple: #a54499;
    --cta-orange: #e57c2c;
    --cta-text: #ffffff;
    --photo-warm: #c9a98a;
    --photo-light: #e6d8c8;
  }
  * { box-sizing: border-box; margin: 0; padding: 0; }
  html, body { width: 1200px; height: 900px; overflow: hidden; }
  body {
    background: var(--page-bg);
    font-family: "Ubuntu", sans-serif;
    color: var(--body-text);
  }
  .services {
    background: linear-gradient(var(--section-bg), var(--page-bg));
    padding-top: 58px;
    height: 640px;
  }
  .services__title {
    font-family: "Lato", sans-serif;
    font-weight: 700;
    font-size: 23px;
    letter-spacing: -0.3px;
    color: var(--heading);
    text-align: center;
  }
  .service-list {
    display: flex;
    justify-content: center;
    gap: 16px;
    margin-top: 66px;
  }
  .service-card {
    width: 266px;
    height: 450px;
    background: var(--card-bg);
    border-radius: 10px;
    box-shadow: 0 10px 24px rgba(0,0,0,0.05);
    overflow: hidden;
    text-align: center;
  }
  .service-card__photo {
    height: 153px;
    border-radius: 10px 10px 0 0;
  }
  .photo--home { background: linear-gradient(120deg, #6b4d3f, #c8b09a 45%, #3e4756); }
  .photo--refinance { background: linear-gradient(120deg, var(--photo-light), #d9c3a5 50%, #a58a72); }
  .photo--investment { background: linear-gradient(120deg, #a7785a, var(--photo-warm) 55%, #e3d7c8); }
  .service-card__name {
    margin-top: 30px;
    font-size: 19px;
    font-weight: 500;
    color: var(--title-purple);
  }
  .service-card__text {
    margin: 16px auto 0;
    width: 212px;
    font-size: 12.3px;
    font-weight: 300;
    line-height: 21.5px;
    color: var(--body-text);
  }
  .button {
    display: inline-block;
    background: var(--cta-orange);
    color: var(--cta-text);
    font-family: "Ubuntu", sans-serif;
    font-weight: 500;
    font-size: 12px;
    text-transform: uppercase;
    text-decoration: none;
    border-radius: 2px;
  }
  .service-card .button {
    margin-top: 20px;
    width: 124px;
    line-height: 36px;
  }
  .service-card--short .button { margin-top: 42px; }
  .cta-band {
    text-align: center;
    padding-top: 30px;
  }
  .cta-band__title {
    font-size: 31px;
    font-weight: 500;
    color: var(--heading);
  }
  .cta-band__text {
    margin-top: 20px;
    font-size: 14.5px;
    font-weight: 300;
    color: var(--body-text);
  }
  .cta-band .button {
    margin-top: 16px;
    width: 160px;
    line-height: 42px;
    font-size: 13px;
  }
</style>
</head>
<body>
  <section class="services">
    <h2 class="services__title">WHAT CAN BRISK LENDING DO FOR YOU</h2>
    <div class="service-list">
      <article class="service-card">
        <div class="service-card__photo photo--home" role="img" aria-label="Friends sharing a meal around a dining table at home"></div>
        <h3 class="service-card__name">Home Loans</h3>
        <p class="service-card__text">Your home loan is likely to be one of your life's biggest investments so you want to make sure you get it right. However, choosing the right loan can be confusing which is where Brisk Lending can help you every step of the way.</p>
        <a class="button" href="#">Learn More</a>
      </article>
      <article class="service-card service-card--short">
        <div class="service-card__photo photo--refinance" role="img" aria-label="Two people shaking hands across a desk"></div>
        <h3 class="service-card__name">Refinance</h3>
        <p class="service-card__text">Refinancing refers to the process of paying out your current home loan by taking out a new loan, either with your existing lender or through a different lender and Brisk Lending are the experts in refinancing.</p>
        <a class="button" href="#">Learn More</a>
      </article>
      <article class="service-card service-card--short">
        <div class="service-card__photo photo--investment" role="img" aria-label="Colleagues reviewing financial charts on a desk"></div>
        <h3 class="service-card__name">Investment Loans</h3>
        <p class="service-card__text">Would you like to make your money work for you? Use your home equity to buy an investment property that will allow you to take advantage of the associated tax benefits and introduce a regular and steady income stream</p>
        <a class="button" href="#">Learn More</a>
      </article>
    </div>
  </section>
  <section class="cta-band">
    <h2 class="cta-band__title">Give us a chance to make a difference</h2>
    <p class="cta-band__text">We're all about helping you reach your next financial goal—great rates, less fees, unprecedented service, and awesome loan help.</p>
    <a class="button" href="#">Book In Now</a>
  </section>
</body>
</html>
```